Heat and air plumbing company needing eye catching van wrap

Looking for van wrap for 2012 Marlow T370. Would like the layout to be like the red blue and white just like the pic I’m sending. Would like the logo to be like the blue van with the ice cubes. So basically I want the red white blue van layout with my logo and the Tilbury Heat air and plumbing should be in black and red and blue and light blue outlined in white. Have website on sides and phone number. On the botttom of the door i want a section in pink with ribbon and breast cancer awareness. On the other side a dog and cat and says adopt a pet. I have several vans and will want a different awareness on each door.
Industry/Entity Type
It Company
Requirements
Must have
- Red blue white layout like the pic. Big logo. Want the layout and colors of the last pic that has white front.

```html
<!DOCTYPE html>
<html lang="en">
<head>
<meta charset="utf-8">
<title>Tilbury Heat Air &amp; Plumbing – Van Wrap</title>
<link rel="stylesheet" href="https://fonts.googleapis.com/css2?family=Archivo+Black&family=Roboto:wght@700;900&display=swap">
<style>
  :root {
    --wrap-blue: #1f56b8;
    --wrap-blue-light: #3a8ae0;
    --wrap-red: #c8141a;
    --wrap-red-dark: #a30f14;
    --van-white: #f3f3f3;
    --van-line: #b9b9b9;
    --glass: #8a8a8a;
    --tyre: #1b1b1b;
    --rim: #cfd2d4;
    --ink: #2a2a2a;
    --phone-blue: #1c5fc9;
    --pink: #f4a6e0;
    --teal: #5ee3e3;
    --mark-grey: #8f9294;
  }
  html, body {
    margin: 0;
    width: 1200px;
    height: 1000px;
    overflow: hidden;
    background: #ffffff;
  }
  .canvas { display: block; width: 1200px; height: 1000px; }
  .plate { font-family: "Roboto", sans-serif; font-weight: 900; font-size: 21px; fill: var(--ink); }
  .phone { font-family: "Roboto", sans-serif; font-weight: 900; font-size: 24px; fill: var(--phone-blue); stroke: #fff; stroke-width: 4px; paint-order: stroke; }
  .web { font-family: "Roboto", sans-serif; font-weight: 900; font-size: 30px; fill: #fff; stroke: var(--ink); stroke-width: 5px; paint-order: stroke; }
  .brand-name { font-family: "Archivo Black", sans-serif; font-size: 56px; fill: var(--ink); stroke: #fff; stroke-width: 6px; paint-order: stroke; }
  .brand-line { font-family: "Archivo Black", sans-serif; font-size: 24px; fill: var(--ink); stroke: #fff; stroke-width: 5px; paint-order: stroke; }
  .cause { font-family: "Roboto", sans-serif; font-weight: 700; font-size: 13px; fill: #222; }
</style>
</head>
<body>
<svg class="canvas" viewBox="0 0 1200 1000" xmlns="http://www.w3.org/2000/svg">
  <defs>
    <path id="van-body" d="M30,330 L35,255 Q40,235 70,225 L200,140 Q260,95 330,70 Q380,55 460,52 L1110,52 Q1170,55 1178,110 L1185,360 L1188,395 L1030,400 A95 95 0 0 0 840,400 L295,400 A95 95 0 0 0 105,400 L30,395 Z"/>
    <clipPath id="body-clip"><use href="#van-body"/></clipPath>
    <radialGradient id="blue-burst" cx="0.45" cy="0.6" r="0.8">
      <stop offset="0" stop-color="var(--wrap-blue-light)"/>
      <stop offset="1" stop-color="var(--wrap-blue)"/>
    </radialGradient>
    <linearGradient id="red-fade" x1="0" y1="0" x2="0" y2="1">
      <stop offset="0" stop-color="var(--wrap-red)"/>
      <stop offset="1" stop-color="var(--wrap-red-dark)"/>
    </linearGradient>

    <g id="van-side">
      <ellipse cx="600" cy="445" rx="560" ry="22" fill="#000" opacity="0.85"/>
      <use href="#van-body" fill="var(--van-white)" stroke="var(--van-line)" stroke-width="2"/>
      <g clip-path="url(#body-clip)">
        <path class="wrap-blue" d="M560,40 L1200,40 L1200,200 C1000,212 820,240 640,300 L560,330 Z" fill="url(#blue-burst)"/>
        <path class="wrap-stripe" d="M400,420 C600,320 850,232 1200,208 L1200,222 C860,245 620,330 430,420 Z" fill="#fff"/>
        <path class="wrap-red" d="M430,420 C620,330 860,245 1200,222 L1200,420 Z" fill="url(#red-fade)"/>
      </g>
      <path class="side-window" d="M300,82 Q340,66 445,64 L445,195 L262,195 Z" fill="var(--glass)"/>
      <path class="windshield" d="M72,222 L200,142 Q240,112 290,86 L250,196 Z" fill="#6f6f6f"/>
      <line x1="455" y1="60" x2="455" y2="395" stroke="var(--van-line)" stroke-width="2"/>
      <line x1="478" y1="60" x2="478" y2="395" stroke="var(--van-line)" stroke-width="2"/>
      <rect x="462" y="245" width="10" height="28" rx="3" fill="#555"/>
      <rect class="bumper-front" x="22" y="325" width="80" height="40" rx="8" fill="#9b9b9b"/>
      <rect class="grille" x="36" y="245" width="34" height="70" rx="4" fill="#4a4a4a"/>
      <rect class="bumper-rear" x="1140" y="340" width="50" height="42" rx="5" fill="#9b9b9b"/>
      <rect class="tail-light" x="1165" y="235" width="18" height="60" rx="3" fill="#b01217"/>
      <g class="wheel">
        <circle cx="200" cy="405" r="78" fill="var(--tyre)"/>
        <circle cx="200" cy="405" r="50" fill="var(--rim)"/>
        <circle cx="200" cy="405" r="16" fill="#8d9093"/>
      </g>
      <g class="wheel">
        <circle cx="935" cy="405" r="78" fill="var(--tyre)"/>
        <circle cx="935" cy="405" r="50" fill="var(--rim)"/>
        <circle cx="935" cy="405" r="16" fill="#8d9093"/>
      </g>
    </g>
  </defs>

  <!-- Driver side (facing left) -->
  <g class="van van--left">
    <use href="#van-side"/>
    <rect class="brand-mark" x="520" y="90" width="220" height="220" rx="28" fill="var(--mark-grey)" stroke="#fff" stroke-width="8" transform="rotate(-8 630 200)"/>
    <text class="brand-name" x="765" y="170">TILBURY</text>
    <text class="brand-line" x="770" y="205">Heat Air &amp; Plumbing</text>
    <text class="web" x="835" y="282">tilburyair.com</text>
    <text class="plate" x="160" y="235">OK 48213</text>
    <rect class="cause-panel cause-panel--pink" x="95" y="250" width="175" height="42" fill="var(--pink)"/>
    <rect x="102" y="255" width="22" height="32" fill="#e0338f" role="img" aria-label="Pink awareness ribbon"/>
    <text class="cause" x="135" y="268">Breast Cancer</text>
    <text class="cause" x="150" y="284">Awareness</text>
    <text class="phone" x="292" y="315">405-555-0188</text>
  </g>

  <!-- Passenger side (facing right) -->
  <g class="van van--right">
    <g transform="translate(1200 470) scale(-1 1)"><use href="#van-side"/></g>
    <rect class="brand-mark" x="460" y="560" width="220" height="220" rx="28" fill="var(--mark-grey)" stroke="#fff" stroke-width="8" transform="rotate(8 570 670)"/>
    <text class="brand-name" x="55" y="640">TILBURY</text>
    <text class="brand-line" x="60" y="675">Heat Air &amp; Plumbing</text>
    <text class="web" x="135" y="752">tilburyair.com</text>
    <text class="plate" x="948" y="706">OK 48213</text>
    <rect class="cause-panel cause-panel--teal" x="936" y="720" width="170" height="45" fill="var(--teal)"/>
    <text class="cause" x="980" y="738">Adopt</text>
    <text class="cause" x="985" y="755">a Pet</text>
    <rect x="1050" y="723" width="50" height="38" fill="#d9d9d9" role="img" aria-label="Dog and cat illustration"/>
    <text class="phone" x="733" y="786">405-555-0188</text>
  </g>
</svg>
</body>
</html>
```